Business / Discount Card

Looking to create a 2 sided business card. Front side to say "Thanks for flying with Skyward Drifts" then have link to "In-Flight Photos, www.skywarddrifts-example.com.au, password: skyward" Back side of card to have company logo, phone number, facebook & instagram logo and #skywarddrifts. Also included on this side will be discount text "Book again and save 10%. Use discount code: skyward10"Round Corner Card Templates are attached. Please ensure dimensions are correct.Thanks,

Font styles to use
Sans Serif

Colors
33a6d7
ffffff
000000

Requirements
Must have
• Logo
• Blue, White and Black color scheme

```html
<!DOCTYPE html>
<html lang="en">
<head>
<meta charset="utf-8">
<title>Skyward Drifts – Discount Card</title>
<link href="https://fonts.googleapis.com/css2?family=Fira+Sans:wght@300;400;500&display=swap" rel="stylesheet">
<style>
  :root {
    --brand-blue: #33a6d7;
    --ink: #050608;
    --paper: #ffffff;
    --rule: rgba(255,255,255,0.75);
    --backdrop: #ececec;
    --sky-top: #a9aec4;
    --sky-mid: #d8b9a6;
    --field: #6b5634;
    --ground-dark: #2a2318;
  }
  * { box-sizing: border-box; margin: 0; padding: 0; }
  html, body { width: 1200px; height: 1200px; overflow: hidden; }
  body {
    background: var(--backdrop);
    font-family: "Fira Sans", Arial, sans-serif;
    color: var(--paper);
    position: relative;
  }
  .card {
    position: absolute;
    left: 268px;
    width: 688px;
    height: 392px;
    border-radius: 32px;
    overflow: hidden;
  }
  .card--offer { top: 155px; background: var(--ink); }
  .card--photo { top: 608px; }

  .brand {
    position: absolute; left: 36px; top: 44px;
    display: flex; align-items: center; gap: 10px;
  }
  .brand__dot {
    width: 26px; height: 26px; border-radius: 50%;
    background: var(--brand-blue);
  }
  .brand__name {
    font-size: 34px; font-weight: 500; color: var(--brand-blue);
    letter-spacing: 0.5px;
  }
  .thanks {
    position: absolute; right: 26px; top: 84px;
    font-size: 22px; font-weight: 300;
  }
  .rule {
    position: absolute; left: 29px; width: 641px; height: 1.5px;
    background: var(--rule);
  }
  .rule--top { top: 133px; }
  .rule--bottom { top: 317px; }

  .offer__headline {
    position: absolute; left: 36px; top: 197px;
    font-size: 30px; font-weight: 400; letter-spacing: 0.6px;
  }
  .offer__code {
    position: absolute; left: 42px; top: 244px;
    font-size: 20px; font-weight: 400; letter-spacing: 0.5px;
  }
  .offer__amount {
    position: absolute; right: 30px; top: 150px;
    font-size: 148px; font-weight: 300; line-height: 1;
  }

  .contact {
    position: absolute; left: 56px; top: 337px;
    display: flex; align-items: center;
    font-size: 17px; font-weight: 400; letter-spacing: 0.3px;
  }
  .contact__item { display: flex; align-items: center; gap: 12px; margin-right: 24px; }
  .contact__icon { width: 21px; height: 21px; flex: none; }
  .contact__square { width: 21px; height: 21px; background: var(--brand-blue); border-radius: 3px; flex: none; }

  .photo {
    position: absolute; inset: 0;
    background: linear-gradient(180deg, var(--sky-top) 0%, var(--sky-mid) 40%, var(--field) 72%, var(--ground-dark) 100%);
  }
  .photo__url {
    position: absolute; left: 52px; top: 333px;
    font-size: 25px; font-weight: 400; letter-spacing: 0.3px;
  }
</style>
</head>
<body>
  <section class="card card--offer">
    <div class="brand">
      <span class="brand__dot"></span>
      <span class="brand__name">Skyward Drifts</span>
    </div>
    <p class="thanks">Thanks for flying with Skyward Drifts</p>
    <div class="rule rule--top"></div>

    <p class="offer__headline">BOOK AGAIN AND SAVE</p>
    <p class="offer__code">DISCOUNT CODE: SKYWARD10</p>
    <p class="offer__amount">10%</p>

    <div class="rule rule--bottom"></div>
    <div class="contact">
      <span class="contact__item">
        <svg class="contact__icon" viewBox="0 0 24 24" aria-hidden="true">
          <path fill="#33a6d7" d="M2 9c0-3 4-5 10-5s10 2 10 5v2h-5V8.5c-1.5-.6-3.2-.9-5-.9s-3.5.3-5 .9V11H2zM6 12l2.5-3h7l2.5 3v8H6zM12 18a3 3 0 1 0 0-6 3 3 0 0 0 0 6z"/>
        </svg>
        1-555-010-2040
      </span>
      <span class="contact__item">
        <span class="contact__square"></span>
        #skywarddrifts
      </span>
      <span class="contact__item">
        <span class="contact__square"></span>
        #skywarddrifts
      </span>
    </div>
  </section>

  <section class="card card--photo">
    <div class="photo" role="img" aria-label="Photo of blue and black hot air balloons inflating on a grassy field at dawn with a crew member holding a rope"></div>
    <p class="photo__url">www.skywarddrifts-example.com.au</p>
  </section>
</body>
</html>
```